OLU58 biz card & Stationery

LU58 is a personalized shopping experience brought to you, that lets you find and discover fashion goods through a collection of boutiques curated by taste-makers - celebrities, stylists, designers, and fashion bloggers. Boutiques uses visual technology to help fashionistas discover and shop their look and creates the opportunity for designers to showcase their collections and latest inspirations online.

OLU58 is built on technology developed by our team of fashion experts who work with engineers to “teach” our computer systems to understand various patterns, pairings, and genre definitions. When signed into your account, OLU58 learns about your style and preferences and in turn, provides you better results and recommendations over time. Ultimately, OLU58 will provide shoppers with a much richer and interactive shopping experience and help drive traffic to retailers' websites.

We need a definitely cool business card. The card must be black! And must use our official logo which can be download from OLU58.com

The address for Letter head and evenlop, please use 4872 Crestwick Parkway, Sutie 510 Los Angeles CA90412, email will be anyone@OLU58.com, website is www.OLU58.com

thanks

We received some of the design, thanks. But most of the design are not what we want. We need a very clean version with black ground, you may also use some dark gray to add the element. please take a look at http://morvalstudio.no/work/#pelter__ostrama/, we do like this kind of design very much. hope it help.

```html
<!DOCTYPE html>
<html lang="en">
<head>
<meta charset="utf-8">
<title>OLU58 Business Card &amp; Stationery</title>
<link rel="stylesheet" href="https://fonts.googleapis.com/css2?family=Roboto+Condensed:wght@300;400&display=swap">
<style>
  :root {
    --canvas: #ffffff;
    --paper: #ffffff;
    --card-front: #231f20;
    --card-back: #3d3d3e;
    --mark-grey: #6f6f70;
    --mark-faint: #58585a;
    --text-light: #e6e6e6;
    --text-muted: #8a8a8a;
    --paper-text: #7a7a7a;
  }
  * { margin: 0; padding: 0; box-sizing: border-box; }
  html, body { width: 1200px; height: 1200px; overflow: hidden; background: var(--canvas); }
  body { position: relative; font-family: "Roboto Condensed", "Arial Narrow", sans-serif; font-weight: 300; }

  .sheet { position: absolute; background: var(--paper); box-shadow: 0 2px 10px rgba(0,0,0,0.12); }
  .wordmark { font-family: "Roboto Condensed", "Arial Narrow", sans-serif; font-weight: 300; line-height: 1; letter-spacing: 0.02em; white-space: nowrap; }

  /* Letterhead */
  .letterhead { left: 0; top: 67px; width: 1111px; height: 760px; }
  .letterhead .wordmark { position: absolute; right: 57px; top: 54px; font-size: 60px; color: var(--paper-text); }
  .letterhead .contact { position: absolute; right: 57px; top: 114px; text-align: right; font-size: 8.5px; line-height: 14px; color: var(--paper-text); letter-spacing: 0.03em; }
  .sep { padding: 0 5px; color: #b5b5b5; }
  .label { font-size: 6px; color: #aaaaaa; padding-right: 3px; }

  /* Business cards */
  .card { position: absolute; width: 498px; height: 263px; overflow: hidden; box-shadow: 0 4px 12px rgba(0,0,0,0.25); }
  .card-back { left: 481px; top: 269px; background: var(--card-back); }
  .card-back .site { position: absolute; left: 44px; bottom: 24px; font-size: 15px; color: var(--mark-grey); }
  .card-back .wordmark-vertical { position: absolute; left: 462px; top: 282px; transform: rotate(-90deg); transform-origin: 0 0; font-size: 118px; color: var(--mark-faint); }

  .card-front { left: 135px; top: 522px; background: var(--card-front); }
  .card-front .wordmark { position: absolute; right: 42px; top: 96px; font-size: 58px; color: var(--mark-grey); }
  .holder { position: absolute; left: 45px; top: 116px; }
  .holder-name { font-size: 13px; font-weight: 400; color: var(--text-light); }
  .holder-role { font-size: 8px; letter-spacing: 0.06em; color: var(--text-muted); margin-top: 3px; }
  .numbers { position: absolute; left: 45px; top: 172px; list-style: none; font-size: 12px; line-height: 16px; color: var(--text-light); }
  .numbers .label { font-size: 6px; color: var(--text-muted); padding-right: 6px; }
  .card-address { position: absolute; right: 42px; top: 172px; text-align: right; font-size: 12px; line-height: 16px; color: var(--text-light); }

  /* Envelope */
  .envelope { left: 140px; top: 813px; width: 1080px; height: 420px; }
  .envelope .wordmark { position: absolute; left: 50px; top: 35px; font-size: 58px; color: var(--paper-text); }
  .envelope .return { position: absolute; left: 51px; top: 90px; font-size: 6px; color: var(--paper-text); letter-spacing: 0.03em; }
</style>
</head>
<body>

<section class="sheet letterhead">
  <div class="wordmark">OLU58</div>
  <div class="contact">
    <div>4872 CRESTWICK PKWY.<span class="sep">|</span>SUITE 510<span class="sep">|</span>LOS ANGELES&nbsp; CA<span class="sep">|</span>90412</div>
    <div><span class="label">T</span>818.555.0142<span class="sep"></span><span class="label">F</span>818.555.0178<span class="sep"></span><span class="label">E</span>info@OLU58.com</div>
  </div>
</section>

<section class="card card-back">
  <div class="site">OLU58.com</div>
  <div class="wordmark wordmark-vertical">OLU58</div>
</section>

<section class="card card-front">
  <div class="wordmark">OLU58</div>
  <div class="holder">
    <div class="holder-name">Mara L. Quinn</div>
    <div class="holder-role">PRINCIPAL</div>
  </div>
  <ul class="numbers">
    <li><span class="label">T</span>818.555.0142</li>
    <li><span class="label">F</span>818.555.0178</li>
    <li><span class="label">M</span>818.555.0196</li>
    <li><span class="label">E</span>mquinn@OLU58.com</li>
  </ul>
  <address class="card-address" style="font-style:normal">
    4872 CRESTWICK PKWY.<br>SUITE 510<br>LOS ANGELES&nbsp; CA<br>90412
  </address>
</section>

<section class="sheet envelope">
  <div class="wordmark">OLU58</div>
  <div class="return">510 · 4872 CRESTWICK PKWY.<span class="sep">|</span>LOS ANGELES&nbsp; CA<span class="sep">|</span>90412</div>
</section>

</body>
</html>
```